Lawn maintenance
Greenmoor has you covered!
weekly , biweekly

Target Market(s)

lawn care

Industry/Entity Type

Lawn Care

Contact Information for Business Card

eye catching - not you normal "lawn business" card

Logo Text

Greenmoor Lawncare

Font styles to use
Serif
Sans Serif

Colors
ec1f27
00a990
9bcb3c
0455a3

Requirements
Must have
• Tom Halvik
• 410-555-0187
• Lawn maintenance
• Greenmoor has you covered!
• Call for a quote today!
• weekly or biweekly
Nice to have
• maybe some poker chips or playing cards
Should not have
• snow removal

```html
<!DOCTYPE html>
<html lang="en">
<head>
<meta charset="utf-8">
<title>Greenmoor Lawncare – Business Card</title>
<link rel="stylesheet" href="https://fonts.googleapis.com/css2?family=Lato:wght@400;700&display=swap">
<style>
  :root {
    --stage: #1e1e1e;
    --card-white: #ffffff;
    --teal: #00a990;
    --lime: #9bcb3c;
    --ink: #111111;
    --rule: #c8c8c8;
    --shadow: rgba(0, 0, 0, 0.55);
  }
  * { margin: 0; padding: 0; box-sizing: border-box; }
  html, body {
    width: 1200px; height: 900px; overflow: hidden;
    background: var(--stage);
    font-family: "Lato", Arial, sans-serif;
  }
  .stage { position: relative; width: 1200px; height: 900px; }
  .card {
    position: absolute; top: 306px;
    width: 440px; height: 271px;
    border-radius: 10px; overflow: hidden;
    box-shadow: 2px 3px 4px var(--shadow);
  }
  .card-front { left: 149px; background: var(--card-white); }
  .card-back { left: 608px; background: var(--lime); }

  .brand-name {
    position: absolute; right: 23px; top: 104px;
    color: var(--teal); font-weight: 700;
    font-size: 25px; line-height: 1.1; letter-spacing: 0.5px;
    text-align: right; text-transform: uppercase;
  }
  .holder-name {
    position: absolute; left: 23px; top: 155px;
    color: var(--teal); font-weight: 700; font-size: 19px;
    text-transform: uppercase;
  }
  .phone-row {
    position: absolute; left: 23px; top: 180px; right: 25px;
    display: flex; align-items: center; gap: 8px;
    font-size: 15px; color: var(--ink);
  }
  .phone-label { color: var(--lime); }
  .phone-rule { flex: 1; height: 1px; background: var(--rule); }

  .tagline {
    position: absolute; top: 214px;
    font-size: 13px; line-height: 17px; color: var(--ink);
    text-transform: uppercase;
  }
  .tagline-left { left: 23px; }
  .tagline-right { right: 23px; text-align: right; font-weight: 700; }
  .edge-bar { position: absolute; top: 216px; width: 11px; height: 28px; }
  .edge-bar-left { left: 0; background: var(--lime); }
  .edge-bar-right { right: 0; background: var(--teal); width: 12px; }

  .back-field { position: absolute; inset: 0; background: var(--lime); }
  .back-name {
    position: absolute; left: 296px; top: 140px; width: 100px;
    color: #ffffff; font-weight: 700; font-size: 13px; line-height: 1.15;
    text-align: center; text-transform: uppercase;
  }
</style>
</head>
<body>
  <main class="stage">
    <section class="card card-front" aria-label="Business card front">
      <div class="brand-name">Greenmoor<br>Lawncare</div>
      <h1 class="holder-name">Tom Halvik</h1>
      <div class="phone-row">
        <span><span class="phone-label">P:</span> 410-555-0187</span>
        <span class="phone-rule"></span>
      </div>
      <span class="edge-bar edge-bar-left"></span>
      <p class="tagline tagline-left">Lawn maintenance<br>Greenmoor has you covered!</p>
      <p class="tagline tagline-right">Call for a quote today!<br>Weekly or biweekly</p>
      <span class="edge-bar edge-bar-right"></span>
    </section>

    <section class="card card-back" aria-label="Business card back">
      <div class="back-field" role="img" aria-label="Green field with faint repeating brand pattern"></div>
      <div class="back-name">Greenmoor<br>Lawncare</div>
    </section>
  </main>
</body>
</html>
```